Open Window; Sunrise Table, River Walk Rack Card

We want an additional 2 page (front and page) 3.67" x 8.5" rack card. This rack card is now the 2nd of the series . The first one is already completed/finalized and attached (Sunrise Table River Walk Rack Card PDF).
Use the text on the word document for the included Open Window Rack card. Please use the Sunrise Table River Walk Rack card as the template to mimic. We would like all subsequent rack cards to have a similar look and feel.
The document is for older readers. Do not put text over graphics and keep it simple and easy to read with high contrast.
We want some very simple design element(s) incorporated that convey Native American communities or heritage. But NO headdress, teepee graphics, etc. At the top, of the first page we would like a collage of healthy food images. This can include fish, chicken, fresh vegetables, berries, brown rice, etc. Please remember to include the funding statement - it can be in a very small font 6/7 point. For more information about our project, please visit https://pelmorvo.org/kite-lane/

```html
<!DOCTYPE html>
<html lang="en">
<head>
<meta charset="utf-8">
<title>Open Window — Sunrise Table River Walk Rack Card</title>
<link href="https://fonts.googleapis.com/css2?family=Open+Sans:wght@700;800&family=Poppins:wght@400;500;600;700;800&family=Roboto:wght@400;700&display=swap" rel="stylesheet">
<style>
  :root {
    --canvas: #e9ecec;
    --panel: #f3f3f2;
    --panel-grain: #ebebea;
    --maroon: #5a1e19;
    --teal: #3fa3ad;
    --teal-deep: #1f6e73;
    --teal-ink: #1d5559;
    --rose: #b0524b;
    --ink: #1b1b1b;
    --white: #ffffff;
  }
  * { margin: 0; padding: 0; box-sizing: border-box; }
  html, body { width: 1104px; height: 1200px; overflow: hidden; }
  body {
    background: var(--canvas);
    font-family: "Poppins", sans-serif;
    color: var(--ink);
    position: relative;
  }
  .panel {
    position: absolute;
    top: 26px;
    height: 1146px;
    background: repeating-linear-gradient(90deg, var(--panel) 0 70px, var(--panel-grain) 70px 72px, var(--panel) 72px 140px);
    overflow: hidden;
  }
  .panel--front { left: 34px; width: 495px; }
  .panel--back { left: 579px; width: 496px; }
  .abs { position: absolute; }

  /* front */
  .food-collage {
    left: 0; top: 0; width: 495px; height: 152px;
    background: linear-gradient(90deg, #8a6a4c 0%, #3a2a26 35%, #c9a24a 50%, #5f8a4a 70%, #c8d7e6 100%);
    border-radius: 0 0 40px 40px;
  }
  .title-main {
    left: 0; width: 495px; top: 150px;
    text-align: center;
    font-family: "Open Sans", sans-serif;
    font-weight: 800;
    font-size: 37px;
    line-height: 46px;
    color: var(--maroon);
    letter-spacing: 0.5px;
  }
  .title-sub {
    left: 0; width: 495px; top: 239px;
    text-align: center;
    font-family: "Open Sans", sans-serif;
    font-weight: 800;
    font-size: 37px;
    color: var(--teal);
    letter-spacing: 0.5px;
  }
  .intro {
    left: 73px; top: 289px; width: 356px;
    font-size: 12.6px; line-height: 16.3px;
  }
  .intro a { color: var(--teal); text-decoration: underline; }
  .changes-heading {
    left: 74px; top: 364px;
    font-weight: 700; font-size: 16px; color: var(--teal-ink);
  }
  .changes-heading span { color: var(--rose); }
  .checklist {
    left: 74px; top: 395px; width: 336px;
    list-style: none;
  }
  .checklist li {
    position: relative;
    padding-left: 33px;
    font-size: 14.6px; line-height: 18px;
    margin-bottom: 6.5px;
  }
  .tick {
    position: absolute; left: 0; top: 1px;
    width: 22px; height: 20px;
  }
  .chevron-band {
    height: 26px;
    background: repeating-linear-gradient(90deg, var(--teal-deep) 0 14px, #8a5a52 14px 28px);
    opacity: 0.85;
  }
  .doctor-band {
    left: 0; top: 787px; width: 495px; height: 61px;
    background: var(--maroon);
    color: var(--white);
  }
  .doctor-icon {
    left: 20px; top: 12px; width: 28px; height: 40px;
    background: var(--white); border-radius: 12px 12px 2px 2px; opacity: 0.9;
  }
  .doctor-band p {
    left: 55px; top: 10px; width: 410px;
    font-weight: 700; font-size: 16px; line-height: 20px; letter-spacing: 0.2px;
  }
  .quote {
    left: 68px; top: 858px; width: 262px;
  }
  .quote-open {
    font-weight: 800; color: var(--teal); font-size: 40px; line-height: 30px; height: 24px;
  }
  .quote blockquote { font-weight: 700; font-size: 16.6px; line-height: 20.3px; color: #2a2a2a; }
  .quote-close { font-weight: 800; color: var(--teal); font-size: 30px; line-height: 0; vertical-align: -8px; }
  .quote cite { display: block; font-style: normal; font-size: 9.5px; margin-top: 8px; }
  .berry-basket {
    left: 334px; top: 865px; width: 147px; height: 136px;
    background: linear-gradient(180deg, #b8233a 0%, #3a3f7a 35%, #d49a6a 45%, #c07b4e 100%);
    border-radius: 20px 20px 40px 40px;
  }
  .web-band {
    left: 0; top: 1001px; width: 495px; height: 40px;
    background: var(--teal-deep);
    color: var(--white);
    text-align: center;
    font-weight: 700; font-size: 23px; line-height: 40px;
  }
  .closing {
    left: 34px; top: 1047px; width: 450px;
    font-weight: 600; font-size: 19px; line-height: 23px; color: var(--teal-ink);
  }
  .funding {
    left: 10px; top: 1110px; width: 478px;
    font-family: "Roboto", sans-serif; font-size: 6.6px; line-height: 10px; color: #333;
  }

  /* back */
  .make-home {
    left: 45px; top: 44px;
    font-family: "Open Sans", sans-serif; font-weight: 800; font-size: 39px;
    color: var(--maroon);
  }
  .make-home span { color: var(--teal); }
  .recipe-title {
    left: 52px; top: 125px; width: 180px;
    font-weight: 400; font-size: 19.5px; line-height: 22px; color: var(--teal-deep);
  }
  .stew-bowl {
    left: 32px; top: 195px; width: 202px; height: 147px;
    background: radial-gradient(ellipse at 50% 30%, #e8d6a8 0%, #b98a52 45%, #6b3f20 100%);
    border-radius: 30px 30px 90px 90px;
  }
  .ingredients-heading {
    left: 308px; top: 118px;
    font-weight: 700; font-size: 19px; color: var(--teal-deep);
  }
  .ingredients {
    left: 256px; top: 155px; width: 232px; list-style: none;
  }
  .ingredients li {
    position: relative; padding-left: 34px;
    font-size: 14.6px; line-height: 18px; margin-bottom: 9px;
  }
  .method {
    left: 44px; top: 366px; width: 430px;
    font-size: 15.9px; line-height: 22.5px;
  }
  .yield {
    left: 0; width: 496px; top: 556px; text-align: center;
    font-size: 19px; color: var(--rose);
  }
  .elders-box {
    left: 0; top: 594px; width: 496px; height: 147px;
    background: var(--maroon); color: var(--white);
  }
  .elders-icon {
    position: absolute; left: 43px; top: 19px; width: 107px; height: 103px;
    background: linear-gradient(180deg, #7a3a33 0%, #6a2c26 100%);
    border-radius: 6px;
  }
  .elders-box p {
    position: absolute; left: 168px; top: 16px; width: 312px;
    font-size: 17.6px; line-height: 21px;
  }
  .info-title {
    left: 0; width: 496px; top: 768px; text-align: center;
    font-family: "Roboto", sans-serif; font-weight: 400; font-size: 34px; color: var(--teal);
  }
  .info-sub {
    left: 0; width: 496px; top: 808px; text-align: center;
    font-family: "Roboto", sans-serif; font-weight: 400; font-size: 29px; color: var(--ink);
  }
  .org-name {
    left: 0; width: 496px; text-align: center;
    font-family: "Roboto", sans-serif; font-weight: 700; font-size: 18px; color: var(--rose);
  }
  .link-pill {
    left: 44px; width: 407px; height: 53px; border-radius: 27px;
    background: var(--maroon); color: var(--white);
    font-family: "Roboto", sans-serif; font-weight: 700; font-size: 18.5px;
    display: flex; align-items: center; justify-content: center;
  }
  .resource-mark {
    left: 124px; top: 1020px; width: 260px; height: 60px;
    display: flex; align-items: center; gap: 12px;
  }
  .resource-mark .dot { width: 56px; height: 56px; border-radius: 50%; background: var(--teal); opacity: 0.8; flex: none; }
  .resource-mark span { font-weight: 600; font-size: 16px; color: var(--teal); white-space: nowrap; }
</style>
</head>
<body>

<section class="panel panel--front">
  <div class="abs food-collage" role="img" aria-label="Collage of healthy foods: grilled chicken, wild rice heart, olive oil, eggs, salad and nuts"></div>

  <h1 class="abs title-main">SUNRISE TABLE<br>RIVER WALK</h1>
  <h2 class="abs title-sub">OPEN WINDOW</h2>

  <p class="abs intro">Making small changes in <a>what</a> and <a>how</a> you eat can make you feel better and stay healthier longer. Healthy food choices may be good for your brain, energy, mood, and health.</p>

  <h3 class="abs changes-heading">Little changes that make <span>a big difference</span></h3>

  <ul class="abs checklist">
    <li><svg class="tick" viewBox="0 0 22 20"><rect x="1" y="3" width="16" height="16" fill="none" stroke="#3fa3ad" stroke-width="2"/><path d="M5 10l4 4 11-12" fill="none" stroke="#b0524b" stroke-width="2.5"/></svg>Start today!</li>
    <li><svg class="tick" viewBox="0 0 22 20"><rect x="1" y="3" width="16" height="16" fill="none" stroke="#3fa3ad" stroke-width="2"/><path d="M5 10l4 4 11-12" fill="none" stroke="#b0524b" stroke-width="2.5"/></svg>Write down what, when, and how much you eat for three days.</li>
    <li><svg class="tick" viewBox="0 0 22 20"><rect x="1" y="3" width="16" height="16" fill="none" stroke="#3fa3ad" stroke-width="2"/><path d="M5 10l4 4 11-12" fill="none" stroke="#b0524b" stroke-width="2.5"/></svg>Set SMART goals (Specific, Measurable, Attainable, Relevant &amp; Timebound),like: “I will eat one piece of fruit at breakfast three times this week.”</li>
    <li><svg class="tick" viewBox="0 0 22 20"><rect x="1" y="3" width="16" height="16" fill="none" stroke="#3fa3ad" stroke-width="2"/><path d="M5 10l4 4 11-12" fill="none" stroke="#b0524b" stroke-width="2.5"/></svg>Make just 1 or 2 changes at a time until they become a habit.</li>
    <li><svg class="tick" viewBox="0 0 22 20"><rect x="1" y="3" width="16" height="16" fill="none" stroke="#3fa3ad" stroke-width="2"/><path d="M5 10l4 4 11-12" fill="none" stroke="#b0524b" stroke-width="2.5"/></svg>Focus more on eating healthy food versus not eating unhealthy food.</li>
    <li><svg class="tick" viewBox="0 0 22 20"><rect x="1" y="3" width="16" height="16" fill="none" stroke="#3fa3ad" stroke-width="2"/><path d="M5 10l4 4 11-12" fill="none" stroke="#b0524b" stroke-width="2.5"/></svg>Make a game plan for the times you get tempted to eat unhealthy foods</li>
    <li><svg class="tick" viewBox="0 0 22 20"><rect x="1" y="3" width="16" height="16" fill="none" stroke="#3fa3ad" stroke-width="2"/><path d="M5 10l4 4 11-12" fill="none" stroke="#b0524b" stroke-width="2.5"/></svg>Involve the whole family in setting goals.</li>
    <li><svg class="tick" viewBox="0 0 22 20"><rect x="1" y="3" width="16" height="16" fill="none" stroke="#3fa3ad" stroke-width="2"/><path d="M5 10l4 4 11-12" fill="none" stroke="#b0524b" stroke-width="2.5"/></svg>Name your main reason to eat healthier and feel better, like “More energy to go to church and tribal cultural events.”</li>
  </ul>

  <div class="abs chevron-band" style="left:0;top:761px;width:495px" role="img" aria-label="Chevron pattern band in teal and brown"></div>

  <div class="abs doctor-band">
    <div class="abs doctor-icon" role="img" aria-label="Doctor icon"></div>
    <p class="abs">Talk to your doctor about healthier eating to make you feel better and stay healthier longer.</p>
  </div>

  <figure class="abs quote">
    <div class="quote-open">“</div>
    <blockquote>When it comes to traditional foods,for me it’s something more than just food, it’s my heritage <span class="quote-close">”</span></blockquote>
    <cite>Marela Tosen (Desert River Nation)</cite>
  </figure>
  <div class="abs berry-basket" role="img" aria-label="Wooden basket of fresh strawberries, blueberries and blackberries"></div>

  <div class="abs web-band">www.pelmorvo.org</div>
  <p class="abs closing">Making small, practical changes can help you achieve your health goals</p>
  <p class="abs funding">This product is supported by a federal public health agency as part of a financial assistance award totaling $348,711 with 100 percent funded by that agency. The contents are those of the author(s) and do not necessarily represent the official views of, nor an endorsement by, the agency or the U.S. Government.</p>
</section>

<section class="panel panel--back">
  <h2 class="abs make-home">MAKE THIS <span>AT HOME</span></h2>
  <h3 class="abs recipe-title">O’odham White Tepary Bean Stew</h3>
  <div class="abs stew-bowl" role="img" aria-label="Wooden bowl of white tepary bean stew with meat"></div>

  <h4 class="abs ingredients-heading">Ingredients:</h4>
  <ul class="abs ingredients">
    <li><svg class="tick" viewBox="0 0 22 20"><rect x="1" y="3" width="16" height="16" fill="none" stroke="#3fa3ad" stroke-width="2"/><path d="M5 10l4 4 11-12" fill="none" stroke="#b0524b" stroke-width="2.5"/></svg>1 cup dried tepary beans, rinsed &amp; picked through (substitute Navy Beans or Great Northern beans)</li>
    <li><svg class="tick" viewBox="0 0 22 20"><rect x="1" y="3" width="16" height="16" fill="none" stroke="#3fa3ad" stroke-width="2"/><path d="M5 10l4 4 11-12" fill="none" stroke="#b0524b" stroke-width="2.5"/></svg>10 cups of water</li>
    <li><svg class="tick" viewBox="0 0 22 20"><rect x="1" y="3" width="16" height="16" fill="none" stroke="#3fa3ad" stroke-width="2"/><path d="M5 10l4 4 11-12" fill="none" stroke="#b0524b" stroke-width="2.5"/></svg>1 tsp. salt</li>
    <li><svg class="tick" viewBox="0 0 22 20"><rect x="1" y="3" width="16" height="16" fill="none" stroke="#3fa3ad" stroke-width="2"/><path d="M5 10l4 4 11-12" fill="none" stroke="#b0524b" stroke-width="2.5"/></svg>1 lb. oxtails, beef short ribs, deer, rabbit, or chicken</li>
  </ul>

  <p class="abs method">Put beans, water, and salt in a stockpot. Bring to a boil, reduce heat and simmer, covered, for one hour and a half. Add meat to the bean mixture, cover and cook for one more hour, or until beans are tender and meat is falling off the bone. If using a crockpot, place water and all other ingredients in the pot, cover, and set to high. Cook for 8 hours or until the meat is falling off the bone and the beans are tender.</p>
  <p class="abs yield">Makes 8 – 10 cups.</p>

  <div class="abs elders-box">
    <div class="elders-icon" role="img" aria-label="Simple line illustration of trees and a sun"></div>
    <p>Elders are our keepers of traditional knowledge about food and ways of life. You play an important role in sharing this knowledge with younger generations</p>
  </div>

  <div class="abs chevron-band" style="left:0;top:743px;width:496px" role="img" aria-label="Chevron pattern band in teal and brown"></div>

  <h3 class="abs info-title">For More Information</h3>
  <h4 class="abs info-sub">About Goal Setting</h4>
  <p class="abs org-name" style="top:841px">Council for Everyday Nutrition</p>
  <div class="abs link-pill" style="top:868px">https://pelmo.link/GoalSettingVideo</div>
  <p class="abs org-name" style="top:933px">Harrowgate Medical Center</p>
  <div class="abs link-pill" style="top:959px">https://pelmo.link/SmartGoalsGuide</div>

  <div class="abs resource-mark">
    <div class="dot"></div>
    <span>Kite Lane Resource Center</span>
  </div>

  <p class="abs funding">This product is supported by a federal public health agency as part of a financial assistance award totaling $348,711 with 100 percent funded by that agency. The contents are those of the author(s) and do not necessarily represent the official views of, nor an endorsement by, the agency or the U.S. Government.</p>
</section>

</body>
</html>
```